Coralbend Pastoral Traders Business Cards

We require business cards revamped with our logo. A few details we would like to use.

1. Round Edges
2. Our logo over the top of a wagyu cattle background photo on one side of the card

Other side of the card has the below details.

1. Person Name (First & Last)
2. Job Position
3. Mobile Number
4. Email Address
5. Website Address

Simple & Neat.

Target Market(s)

Sales

Industry/Entity Type

Agriculture

Contact Information for Business Card

CORALBEND PASTORAL TRADERS

Colors

Designer to choose colors to be used in the design.

Requirements
Must have
• Company Logo

```html
<!DOCTYPE html>
<html lang="en">
<head>
<meta charset="UTF-8">
<title>Coralbend Pastoral Traders – Business Cards</title>
<link rel="stylesheet" href="https://fonts.googleapis.com/css2?family=Montserrat:wght@400;500;700&display=swap">
<style>
  :root {
    --bg: #2c2c2c;
    --card: #ffffff;
    --maroon: #6b1a2c;
    --maroon-soft: #efe6e6;
    --ink: #3a2a2c;
    --sky: #e6eaf2;
    --pasture: #eef0e4;
    --cattle: #9a6a5a;
  }
  * { box-sizing: border-box; margin: 0; padding: 0; }
  html, body { width: 1200px; height: 900px; overflow: hidden; }
  body {
    background: var(--bg);
    font-family: "Montserrat", sans-serif;
    position: relative;
  }
  .card {
    position: absolute;
    left: 250px;
    width: 700px;
    height: 400px;
    border-radius: 26px;
    background: var(--card);
    overflow: hidden;
  }
  .card--front { top: 40px; }
  .card--back { top: 460px; }

  /* front */
  .front-mark {
    position: absolute;
    right: 70px;
    top: 60px;
    width: 250px;
    height: 250px;
    border-radius: 50%;
    background: var(--maroon-soft);
  }
  .brand {
    position: absolute;
    left: 40px;
    top: 46px;
    display: flex;
    align-items: center;
    gap: 10px;
    color: var(--maroon);
    font-weight: 700;
    font-size: 22px;
    letter-spacing: 0.5px;
    line-height: 1.1;
  }
  .brand__dot {
    width: 14px; height: 14px; border-radius: 50%;
    background: var(--maroon);
  }
  .person {
    position: absolute;
    left: 80px;
    top: 150px;
    color: var(--ink);
  }
  .person__name {
    color: var(--maroon);
    font-weight: 700;
    font-size: 26px;
  }
  .person__role { font-size: 16px; margin-top: 2px; }
  .person__address { font-size: 15px; margin-top: 20px; line-height: 1.35; }
  .contacts {
    list-style: none;
    position: absolute;
    left: 80px;
    top: 290px;
    font-size: 15px;
    color: var(--ink);
  }
  .contacts li {
    display: flex; align-items: center; gap: 12px;
    margin-bottom: 8px;
  }
  .contacts svg { width: 14px; height: 14px; fill: var(--maroon); }

  /* back */
  .pasture-photo {
    position: absolute; inset: 0;
    background:
      radial-gradient(ellipse 55% 60% at 58% 62%, rgba(154,106,90,0.45), transparent 70%),
      linear-gradient(180deg, var(--sky) 0%, #f1f2ee 45%, var(--pasture) 100%);
  }
  .back-brand {
    position: absolute;
    left: 0; right: 0;
    top: 170px;
    text-align: center;
    color: var(--maroon);
    font-weight: 700;
    font-size: 36px;
    letter-spacing: 1px;
  }
</style>
</head>
<body>
  <section class="card card--front">
    <div class="front-mark" aria-hidden="true"></div>
    <div class="brand"><span class="brand__dot"></span>CORALBEND PASTORAL TRADERS</div>
    <div class="person">
      <p class="person__name">Dorian Halloway</p>
      <p class="person__role">Managing Director</p>
      <p class="person__address">48 Saltbush Road<br>Rockhampton, QLD 4700</p>
    </div>
    <ul class="contacts">
      <li><svg viewBox="0 0 24 24"><path d="M6.6 10.8a15 15 0 0 0 6.6 6.6l2.2-2.2a1 1 0 0 1 1-.25 11.4 11.4 0 0 0 3.6.57 1 1 0 0 1 1 1V20a1 1 0 0 1-1 1A17 17 0 0 1 3 4a1 1 0 0 1 1-1h3.5a1 1 0 0 1 1 1c0 1.25.2 2.45.57 3.57a1 1 0 0 1-.25 1z"/></svg>555.214.7390</li>
      <li><svg viewBox="0 0 24 24"><path d="M2 5h20v14H2z M2 5l10 8 10-8" /></svg>hello@coralbendtraders.com</li>
      <li><svg viewBox="0 0 24 24"><circle cx="12" cy="12" r="10"/></svg>www.coralbendtraders.com</li>
    </ul>
  </section>

  <section class="card card--back">
    <div class="pasture-photo" role="img" aria-label="Soft-focus photo of wagyu cattle standing in a green paddock"></div>
    <p class="back-brand">CORALBEND PASTORAL TRADERS</p>
  </section>
</body>
</html>
```